High-end Management Consulting Website

I am looking for a design that feels very high end and professional and very serious feeling. I would like a site that uses a lot of white space, with colors in the blue, grey family. You can use a very small about of the orange and green in the logo, but it needs to be a very small amount.

I like images similar to a rock climber helping another one up a mountain. I would love other imagery throughout the site of mountain ranges and people making it to the top.

When you think of the feel imagine people in suites, very corporate feeling. Very much focused on helping company leadership and CEOs solve problems.

From a functionality standpoint https://ninebramwell.com has a good deal of similar content- However, I do not like the colors or the design. I like graphics on websites similar to https://www.harrowcapitalgroup.com.

I like clean with lots of white space.

The link below has all of the content and design comments. https://files.quillnet.com/doc/7QpLm3XzR8vTt2KwYh5NbD9sFgJc4EuA6oViWr0Ue/view?share=open

Target Market(s)

High end businesses and very experienced executives.

Industry/Entity Type

Consulting

Coding

Coded - Design and coding required

Number of Pages Required

5+ page

Font styles to use
Sans Serif

Colors

Designer to choose colors to be used in the design.

Requirements
Must have
• white space, blues some gray, clean feel VERY LITTLE use of accent colors.

I want to have a centered navigation bar.
I would like to have a secondary scrolling image.
Nice to have
• High end imagery that speaks to what is being said in the site.
This is not the main image I want to see but I like imagery like this for the main home page.
https://www.pixelmarrow.com/image-photo/couple-hiking-help-each-other-silhouette-731864205
Should not have
• Please do not use dated images or blocky feeling. Please also do not go overboard using the icon in the design.

```html
<!DOCTYPE html>
<html lang="en">
<head>
<meta charset="utf-8">
<title>Summit Crest Partners</title>
<link rel="stylesheet" href="https://fonts.googleapis.com/css2?family=Montserrat:wght@400;500;600&family=Oswald:wght@500;600&family=Raleway:wght@500;600;700&display=swap">
<style>
:root{
  --blue:#2a7fc1;
  --blue-dark:#1f6aa6;
  --ink:#3a3a3a;
  --ink-soft:#6e6e6e;
  --grey-band:#f5f5f5;
  --line:#d9d9d9;
  --white:#ffffff;
  --charcoal:#333333;
  --badge:#dfe3e7;
}
*{box-sizing:border-box;margin:0;padding:0}
html,body{width:1200px;height:3357px;overflow:hidden}
body{font-family:"Montserrat",sans-serif;color:var(--ink);background:var(--white);position:relative}
.block{position:absolute;left:0;width:1200px}
.center{text-align:center}
.eyebrow{font-family:"Raleway",sans-serif;font-weight:500;font-size:15px;color:var(--blue);letter-spacing:.3px}
.section-title{font-family:"Raleway",sans-serif;font-weight:600;font-size:27px;color:#555;letter-spacing:1px;text-transform:uppercase;margin-top:6px}
.btn{display:inline-flex;align-items:center;justify-content:center;background:var(--blue);color:var(--white);font-family:"Raleway",sans-serif;font-weight:600;font-size:14px;border-radius:3px;text-transform:uppercase;letter-spacing:-.2px}
.abs{position:absolute}

/* header */
.topbar{top:0;height:37px}
.topbar-bg{position:absolute;left:495px;right:0;top:0;height:37px;background:#f4f4f4;clip-path:polygon(0 0,100% 0,100% 100%,22px 100%)}
.topbar-info{position:absolute;left:541px;top:10px;font-size:13px;font-weight:500;color:var(--ink);display:flex;gap:36px;align-items:center}
.topbar-info span{display:flex;align-items:center;gap:8px}
.social{position:absolute;left:948px;top:13px;display:flex;gap:11px}
.social i{width:11px;height:11px;border-radius:50%;background:#777;display:block}
.brand{position:absolute;left:160px;top:36px;display:flex;align-items:center;gap:10px}
.brand-mark{width:20px;height:20px;background:var(--blue)}
.brand-name{font-family:"Montserrat",sans-serif;font-weight:600;font-size:16px;color:#2c3e50;letter-spacing:.3px;line-height:1.15}
.nav{position:absolute;top:66px;left:513px;display:flex;font-family:"Raleway",sans-serif;font-weight:600;font-size:13px;color:#555}
.nav a{color:inherit;text-decoration:none;padding:0 20px;position:relative}
.nav a.active{color:var(--blue)}
.nav a.active::after{content:"";position:absolute;left:0;right:0;top:46px;height:3px;background:var(--blue)}

/* hero */
.hero{top:115px;height:491px;background:linear-gradient(100deg,#3c4448 0%,#4d585e 35%,#3b4d62 70%,#1f2f48 100%)}
.hero-kicker{position:absolute;left:160px;top:168px;font-family:"Oswald",sans-serif;font-weight:500;font-size:26px;color:var(--white);letter-spacing:.2px}
.hero-title{position:absolute;left:160px;top:200px;font-family:"Oswald",sans-serif;font-weight:600;font-size:60px;color:var(--white);line-height:1;letter-spacing:-.5px}
.hero .btn{position:absolute;left:161px;top:284px;width:143px;height:44px;font-size:15px}

/* intro */
.intro{top:606px;height:171px;background:var(--grey-band)}
.intro p{width:900px;margin:40px auto 0;font-size:17.5px;line-height:29px;color:#333;text-align:center}

/* about */
.about{top:777px;height:602px}
.about .eyebrow{margin-top:76px}
.about .lead{width:830px;margin:16px auto 0;font-weight:600;font-size:15px;line-height:27px;color:#222}
.about .sub{width:820px;margin:8px auto 0;font-size:15px;line-height:27px;color:#444}
.team{position:absolute;top:285px;left:0;width:1200px;height:170px}
.member{position:absolute;top:0;width:190px;height:170px}
.member svg{display:block}
.member-name{position:absolute;bottom:10px;left:0;right:0;text-align:center;color:var(--white);font-size:14px;font-weight:500}
.arrow{position:absolute;width:26px;height:26px;border-radius:50%;background:var(--white);box-shadow:0 1px 5px rgba(0,0,0,.2);display:flex;align-items:center;justify-content:center;color:#666;font-size:14px}
.about .btn{position:absolute;left:541px;top:487px;width:118px;height:36px}

/* experience */
.experience{top:1379px;height:319px;background:var(--grey-band)}
.experience .eyebrow{margin-top:80px}
.clients{position:absolute;top:155px;left:162px;display:flex;gap:12px}
.client{width:166px;height:86px;background:var(--white);display:flex;align-items:center;justify-content:center}
.client-badge{width:110px;height:34px;border-radius:3px;background:var(--badge)}

/* services */
.services{top:1698px;height:489px}
.services .eyebrow{margin-top:78px}
.service{position:absolute;top:156px;width:200px;text-align:center}
.service h3{font-family:"Montserrat",sans-serif;font-weight:500;font-size:17px;line-height:21px;color:#222;margin-top:14px;text-transform:uppercase}
.service p{font-size:13px;line-height:20px;color:#777;margin-top:6px}
.services .btn{position:absolute;left:537px;top:378px;width:126px;height:36px}

/* banner */
.banner{top:2187px;height:308px;background:linear-gradient(135deg,#2578bd 0%,#2d83c6 50%,#2272b5 100%)}
.banner h2{font-family:"Raleway",sans-serif;font-weight:700;font-size:26px;color:var(--white);letter-spacing:.6px;margin-top:70px;text-transform:uppercase}
.banner p{font-size:22px;line-height:31px;color:var(--white);font-weight:500;margin-top:12px}
.banner .btn{background:var(--charcoal);width:210px;height:36px;margin-top:18px;font-size:14px}

/* contact */
.contact-card{position:absolute;top:2567px;left:248px;width:705px;height:430px;background:#f4f4f4}
.contact-card .eyebrow{margin-top:46px}
.field{position:absolute;height:36px;border:1px solid var(--line);background:var(--white);font-size:13px;color:#888;padding:10px 15px;text-align:left}
.field.message{height:89px}
.contact-card .btn{position:absolute;left:303px;top:338px;width:98px;height:36px}
.fold{position:absolute;left:0;bottom:-2px;width:0;height:0;border-top:37px solid var(--blue);border-right:37px solid transparent}
.card-shadow{position:absolute;top:2994px;left:270px;width:660px;height:18px;border-radius:50%;background:radial-gradient(ellipse at center,rgba(0,0,0,.22),rgba(0,0,0,0) 70%)}

/* footer */
.footer{top:3071px;height:248px;background:linear-gradient(180deg,#eeeeee,#e2e4e6)}
.footer-nav{position:absolute;top:74px;left:0;width:1200px;font-family:"Raleway",sans-serif;font-size:13px;font-weight:500;color:#333}
.footer-nav span{position:absolute;transform:translateX(-50%)}
.contact-item{position:absolute;top:134px;display:flex;align-items:center;gap:12px;font-size:13px;font-weight:500;line-height:20px;color:#222}
.copyright{top:3319px;height:38px;background:var(--blue);color:var(--white);font-size:13px;display:flex;align-items:center;justify-content:center}
</style>
</head>
<body>

<header class="block topbar">
  <div class="topbar-bg"></div>
  <div class="topbar-info">
    <span><svg width="12" height="12" viewBox="0 0 24 24"><path fill="#2a7fc1" d="M6.6 10.8a15 15 0 0 0 6.6 6.6l2.2-2.2c.3-.3.7-.4 1-.2 1.1.4 2.3.6 3.6.6.6 0 1 .4 1 1V20c0 .6-.4 1-1 1A17 17 0 0 1 3 4c0-.6.4-1 1-1h3.5c.6 0 1 .4 1 1 0 1.3.2 2.5.6 3.6.1.3 0 .7-.2 1z"/></svg>Call Us: 555 010 2040</span>
    <span><svg width="13" height="10" viewBox="0 0 26 20"><rect width="26" height="20" rx="2" fill="#2a7fc1"/><path d="M1 2l12 9 12-9" stroke="#fff" stroke-width="2" fill="none"/></svg>hello@summitcrest.example</span>
  </div>
  <div class="social"><i></i><i></i><i></i><i></i></div>
</header>

<div class="brand"><span class="brand-mark"></span><span class="brand-name">SUMMIT CREST<br>PARTNERS</span></div>

<nav class="nav">
  <a class="active">HOME</a><a>SERVICES</a><a>ABOUT ▾</a><a>WORK WITH US</a><a>CONTACT US</a>
</nav>

<section class="block hero" role="img" aria-label="Executives in suits meeting around a conference table in a glass office">
  <div class="hero-kicker">IN TIMES OF ECONOMIC UNCERTAINTY</div>
  <div class="hero-title">YOU NEED AN EDGE</div>
  <a class="btn">GET STARTED</a>
</section>

<section class="block intro">
  <p>As industry leaders, former company founders, active investors and senior innovation experts, we bring experience, knowledge and connections to our engagements. Leading to cost and time savings, higher opportunity utilization and better business outcomes.</p>
</section>

<section class="block about center">
  <div class="eyebrow">ABOUT US</div>
  <h2 class="section-title">Summit Crest - Partners</h2>
  <p class="lead">Our partners have served in executive leadership for fortune 1000 global organizations, served at the highest levels of office and managed billions in buy and sell side transactions.</p>
  <p class="sub">Our experience, founding, scaling, exiting and acquiring companies along the way, gives our team a unique understanding of the clients we serve.</p>
  <div class="team">
    <div class="arrow" style="left:121px;top:72px">‹</div>
    <div class="member" style="left:175px" role="img" aria-label="Portrait of partner Alan in a navy suit">
      <svg width="190" height="170"><defs><linearGradient id="g1" x1="0" y1="0" x2="0" y2="1"><stop offset="0" stop-color="#c9cdd2"/><stop offset="1" stop-color="#2c3e60"/></linearGradient></defs><polygon points="47,0 143,0 190,85 143,170 47,170 0,85" fill="url(#g1)"/></svg>
      <div class="member-name">Alan</div></div>
    <div class="member" style="left:396px" role="img" aria-label="Portrait of partner Ben in a dark suit">
      <svg width="190" height="170"><polygon points="47,0 143,0 190,85 143,170 47,170 0,85" fill="url(#g1)"/></svg>
      <div class="member-name">Ben</div></div>
    <div class="member" style="left:615px" role="img" aria-label="Portrait of partner Cyrus in a blue blazer">
      <svg width="190" height="170"><polygon points="47,0 143,0 190,85 143,170 47,170 0,85" fill="url(#g1)"/></svg>
      <div class="member-name">Cyrus</div></div>
    <div class="member" style="left:833px" role="img" aria-label="Portrait of partner Neil in a dark shirt">
      <svg width="190" height="170"><polygon points="47,0 143,0 190,85 143,170 47,170 0,85" fill="url(#g1)"/></svg>
      <div class="member-name">Neil</div></div>
    <svg class="abs" style="left:1049px;top:70px" width="30" height="28"><polygon points="8,0 22,0 30,14 22,28 8,28 0,14" fill="#2a7fc1"/><path d="M13 9l5 5-5 5" stroke="#fff" stroke-width="1.6" fill="none"/></svg>
  </div>
  <a class="btn">VIEW ALL</a>
</section>

<section class="block experience center">
  <div class="eyebrow">EXPERIENCE</div>
  <h2 class="section-title">Our Experience</h2>
  <div class="arrow" style="left:121px;top:183px">‹</div>
  <div class="clients">
    <div class="client" role="img" aria-label="Client badge"><span class="client-badge"></span></div>
    <div class="client" role="img" aria-label="Client badge"><span class="client-badge"></span></div>
    <div class="client" role="img" aria-label="Client badge"><span class="client-badge"></span></div>
    <div class="client" role="img" aria-label="Client badge"><span class="client-badge"></span></div>
    <div class="client" role="img" aria-label="Client badge"><span class="client-badge"></span></div>
  </div>
  <div class="arrow" style="left:1050px;top:183px">›</div>
</section>

<section class="block services center">
  <div class="eyebrow">SERVICES</div>
  <h2 class="section-title">How We Help</h2>
  <div class="service" style="left:170px">
    <svg width="84" height="78"><polygon points="21,1 63,1 83,39 63,77 21,77 1,39" fill="none" stroke="#2a7fc1" stroke-width="1.5"/><rect x="30" y="42" width="24" height="14" fill="none" stroke="#2a7fc1" stroke-width="1.5"/><circle cx="42" cy="32" r="6" fill="none" stroke="#2a7fc1" stroke-width="1.5"/></svg>
    <h3>Advisory<br>Services</h3>
    <p>Lorem ipsum dolor sit amet, consectetuer adipiscing elit sed diam nonummy</p></div>
  <div class="service" style="left:389px">
    <svg width="84" height="78"><polygon points="21,1 63,1 83,39 63,77 21,77 1,39" fill="none" stroke="#5bab5e" stroke-width="1.5"/><rect x="35" y="32" width="14" height="14" fill="none" stroke="#5bab5e" stroke-width="1.5"/><circle cx="42" cy="22" r="3" fill="#5bab5e"/><circle cx="42" cy="56" r="3" fill="#5bab5e"/><circle cx="25" cy="39" r="3" fill="#5bab5e"/><circle cx="59" cy="39" r="3" fill="#5bab5e"/></svg>
    <h3>Business Model<br>Design</h3>
    <p>Lorem ipsum dolor sit amet, consectetuer adipiscing elit sed diam nonummy</p></div>
  <div class="service" style="left:610px">
    <svg width="84" height="78"><polygon points="21,1 63,1 83,39 63,77 21,77 1,39" fill="none" stroke="#e1653a" stroke-width="1.5"/><circle cx="34" cy="33" r="7" fill="none" stroke="#e1653a" stroke-width="1.5"/><circle cx="50" cy="33" r="7" fill="none" stroke="#e1653a" stroke-width="1.5"/><path d="M30 56v-12M42 56v-12M54 56v-12" stroke="#e1653a" stroke-width="1.5"/></svg>
    <h3>Turnaround and<br>Restructuring</h3>
    <p>Lorem ipsum dolor sit amet, consectetuer adipiscing elit sed diam nonummy</p></div>
  <div class="service" style="left:829px">
    <svg width="84" height="78"><polygon points="21,1 63,1 83,39 63,77 21,77 1,39" fill="none" stroke="#2a7fc1" stroke-width="1.5"/><circle cx="42" cy="30" r="8" fill="none" stroke="#2a7fc1" stroke-width="1.5"/><path d="M30 56v-8M38 56v-12M46 56v-12M54 56v-8" stroke="#2a7fc1" stroke-width="1.5"/></svg>
    <h3>Revenue<br>Enhancement</h3>
    <p>Lorem ipsum dolor sit amet, consectetuer adipiscing elit sed diam nonummy</p></div>
  <a class="btn">GET STARTED</a>
</section>

<section class="block banner center" role="img" aria-label="Blue world map background with market data figures">
  <h2>Global Experience. Local Market Expertise.</h2>
  <p>Our Network of International Business C-Suite Executives<br>Represents Every Major Business Sector.</p>
  <a class="btn">READY TO LEARN MORE</a>
</section>

<section class="contact-card center">
  <div class="eyebrow">INQUIRY</div>
  <h2 class="section-title">Contact Us</h2>
  <div class="field" style="left:59px;top:122px;width:286px">First Name</div>
  <div class="field" style="left:359px;top:122px;width:286px">Last Name</div>
  <div class="field" style="left:59px;top:175px;width:286px">Phone</div>
  <div class="field" style="left:359px;top:175px;width:286px">Email</div>
  <div class="field message" style="left:59px;top:229px;width:586px">Message</div>
  <a class="btn">SUBMIT</a>
  <div class="fold"></div>
</section>
<div class="card-shadow"></div>

<footer class="block footer" role="img" aria-label="Faded city skyline background">
  <div class="footer-nav">
    <span style="left:297px">HOME</span><span style="left:425px">SERVICES</span><span style="left:555px">ABOUT</span><span style="left:706px">WORK WITH US</span><span style="left:877px">CONTACT US</span>
  </div>
  <div class="contact-item" style="left:194px">
    <svg width="48" height="44"><polygon points="12,0 36,0 48,22 36,44 12,44 0,22" fill="#2a7fc1"/><path d="M24 12a7 7 0 0 0-7 7c0 5 7 13 7 13s7-8 7-13a7 7 0 0 0-7-7z" fill="#fff"/><circle cx="24" cy="19" r="2.5" fill="#2a7fc1"/></svg>
    <div>48 Harbor Lane, Suite 900<br>Ashford, ST 10452</div></div>
  <div class="contact-item" style="left:559px">
    <svg width="48" height="44"><polygon points="12,0 36,0 48,22 36,44 12,44 0,22" fill="#2a7fc1"/><path d="M18 15c1 6 5 11 12 13l2-3-3-2-2 1c-2-1-4-3-5-5l1-2-2-3z" fill="#fff"/></svg>
    <div>Call Us<br>555 010 2041</div></div>
  <div class="contact-item" style="left:806px">
    <svg width="48" height="44"><polygon points="12,0 36,0 48,22 36,44 12,44 0,22" fill="#2a7fc1"/><rect x="15" y="15" width="18" height="13" fill="none" stroke="#fff" stroke-width="1.6"/><path d="M15 15l9 7 9-7" stroke="#fff" stroke-width="1.6" fill="none"/></svg>
    <div>Email Us<br>hello@summitcrest.example</div></div>
</footer>

<div class="block copyright">Copyright © 2020 SUMMIT CREST - PARTNERS. All Rights Reserved.</div>

</body>
</html>
```